New brand for digital company - your chance to get creative

We need to create a brand for our new business 'Lanternfish Digital'. Please read the brief below before progressing as we are looking for some quite specific outputs.

Background

We are positioning ourselves as ‘marketing technologists’ - we're helping businesses engage with their customers in the online space.

Our tactics include branding, marketing, online management, and social media, however we are differentiating ourselves by focusing on overall strategy, not just tactics. Our tagline is ‘Online made simple’.

We have stipulated some parameters for the brand but otherwise want designers to exercise their creativity.

Requirements
Must have
• We want to see an entire concept, not just a logo.

```html
<!DOCTYPE html>
<html lang="en">
<head>
<meta charset="utf-8">
<title>Lanternfish Digital – We are marketing technologists</title>
<link rel="stylesheet" href="https://fonts.googleapis.com/css2?family=Bebas+Neue&family=Open+Sans:wght@300;400&display=swap">
<style>
  :root {
    --brand-orange: #f5831f;
    --band-orange: rgba(236, 120, 20, 0.88);
    --ink: #1d1d1d;
    --paper: #ffffff;
    --photo-dark: #3a3a3a;
    --photo-mid: #8a8a8a;
    --photo-light: #cfcfcf;
  }
  html, body {
    margin: 0;
    padding: 0;
    overflow: hidden;
    background: var(--paper);
  }
  .page {
    position: relative;
    width: 900px;
    height: 1200px;
    overflow: hidden;
    background: var(--paper);
  }
  .hero-photo {
    position: absolute;
    left: 0;
    top: 0;
    width: 900px;
    height: 546px;
    background:
      radial-gradient(ellipse 420px 200px at 640px 120px, var(--photo-light), transparent 70%),
      radial-gradient(ellipse 300px 120px at 300px 470px, #b4b4b4, transparent 70%),
      linear-gradient(180deg, var(--photo-dark) 0%, var(--photo-mid) 45%, #6d6d6d 80%, #555 100%);
  }
  .brand-band {
    position: absolute;
    left: 0;
    top: 123px;
    width: 900px;
    height: 295px;
    background: var(--band-orange);
  }
  .brand-lockup {
    position: absolute;
    left: 120px;
    top: 170px;
    color: var(--paper);
    font-family: "Open Sans", sans-serif;
    font-weight: 300;
  }
  .brand-name {
    margin: 0;
    font-size: 80px;
    line-height: 1.1;
    font-weight: 300;
    letter-spacing: 1px;
  }
  .brand-tagline {
    margin: 14px 0 0 4px;
    font-size: 22px;
    font-weight: 300;
    letter-spacing: 3px;
  }
  .intro {
    position: absolute;
    left: 122px;
    top: 600px;
    width: 640px;
  }
  .intro-heading {
    margin: 0;
    font-family: "Bebas Neue", sans-serif;
    font-weight: 400;
    font-size: 87px;
    line-height: 76px;
    color: var(--brand-orange);
  }
  .intro-copy {
    margin: 36px 0 0;
    font-family: "Open Sans", sans-serif;
    font-size: 14.6px;
    line-height: 22px;
    color: var(--ink);
    white-space: nowrap;
  }
  .intro-copy + .intro-copy {
    margin-top: 22px;
  }
</style>
</head>
<body>
  <main class="page">
    <div class="hero-photo" role="img" aria-label="Black and white photograph of a sliced loaf of bread on a wooden board"></div>
    <div class="brand-band"></div>
    <header class="brand-lockup">
      <p class="brand-name">Lanternfish Digital</p>
      <p class="brand-tagline">Online made simple</p>
    </header>

    <section class="intro">
      <h1 class="intro-heading">We are marketing<br>technologists</h1>
      <p class="intro-copy">Utestrumqui beati debit quam quatur, utem arum eribus nonseri osaperem. Ita veligenis<br>dolupti odi cus quod evel iur? Ma nostio corera atum, que nisi suntis natur?<br>Sin re, ut officaborum quaerum dolupta volut quamus idio. Itasped magnimin nonse<br>nonsedi doloribus, tecero te simperis eos eiusae sinus ea aces qui dolenimus doluptate non<br>net mos volum eos dellacc aesequi autassuntum faccuste porro il magnita tenist quatur<br>simaion explabore con eturehent unt,.</p>
      <p class="intro-copy">Acerum et untur? Nam que voluptur, coriae omnis accum is sus vidit aut ommolum, ut<br>eos dollandam a ipsanduci dis in peruntem. Ita deliquatus ea voloreped ma disquas ad que<br>optum ullia dit la veribus descid ut occusa pos evelluptatem apid que is ut harum acia sitate<br>volorep rerspellut int ad eictaqui sitatem pelignimi, consequ odictios volorem de dolorem<br>harum velenimi, quid ma deligendi ipiendae comniet eaqui id quam volupie nistrumque<br>sinctorum coresed molo ea archil millat. Agnis ex erore nos aliam, quas il molesciat.</p>
    </section>
  </main>
</body>
</html>
```